sailbrightly Website for children with diabilities

Hi, we are looking for a new website design for our community service "sailbrightly". Sailbrightly gives children who suffer from diseases or disabilities a week off on a Boat to give the children new hope and an unforgettable experience.

The current website is really old and we want to have a new one.
Please feel free to discover our website under http://sailbrightly-example.at/.
We have several company sponsors which are very important to us.

The Website has to be a Bootstrap Design (Version 4.4 or higher) [NOT Wordpress, Joomla, other CMS]

Target Market(s)

no target market. we like to inform our communities about our service.

Industry/Entity Type

community service for children with disabilities

Coding

Number of Pages Required

4 page

Font styles to use
Sans Serif

Colors
0054AA
0677BA
7BADD7
CADEEF
E8F1F8
0094D4
00A9DD
6FCCEA
C7EBF8
E9F6FB

Requirements
Must have
• About, Sponsors, Information about cruises
Nice to have
• Gallery

```html
<!DOCTYPE html>
<html lang="en">
<head>
<meta charset="utf-8">
<title>Verein Sail Brightly</title>
<link rel="stylesheet" href="https://fonts.googleapis.com/css2?family=Open+Sans:ital,wght@0,300;0,400;0,600;0,700;1,300&display=swap">
<style>
  :root {
    --navy: #1d2a4d;
    --navy-deep: #1b2547;
    --white: #ffffff;
    --body-grey: #5a5f6e;
    --footer: #8fa8ba;
    --icon-tint: #e8f1f8;
    --icon-line: #0677ba;
    --hero-a: #8c8fae;
    --hero-b: #6f6f86;
    --sky-a: #2f68c4;
    --sky-b: #7fb0de;
    --haze-a: #d6e2ea;
    --haze-b: #3d5a72;
    --dusk-a: #7b87a6;
    --dusk-b: #2a3656;
    --sea-a: #2c4f7e;
    --sea-b: #1e3c66;
  }
  * { margin: 0; padding: 0; box-sizing: border-box; }
  html, body { width: 1200px; height: 4777px; overflow: hidden; }
  body { position: relative; background: var(--white); font-family: "Open Sans", Arial, sans-serif; color: var(--navy); }
  .abs { position: absolute; }
  .photo { position: absolute; }

  /* header / hero */
  .hero { left: 0; top: 0; width: 1200px; height: 677px; background: linear-gradient(170deg, var(--hero-a), var(--hero-b)); }
  .brand { position: absolute; display: flex; align-items: center; gap: 16px; }
  .brand-dot { width: 78px; height: 78px; border-radius: 50%; background: var(--navy-deep); }
  .brand-name { font-size: 24px; font-weight: 400; color: var(--navy); }
  .site-header .brand { left: 83px; top: 33px; }
  .nav { position: absolute; display: flex; gap: 28px; font-size: 15px; font-weight: 400; color: var(--white); }
  .nav a { color: inherit; text-decoration: none; }
  .nav .current { font-weight: 700; }
  .site-header .nav { left: 790px; top: 60px; }
  .hero-quote { left: 297px; top: 250px; width: 640px; font-size: 40px; font-weight: 600; line-height: 52px; color: var(--white); }
  .hero-author { left: 297px; top: 418px; width: 560px; text-align: center; font-size: 30px; font-style: italic; font-weight: 300; color: var(--white); }

  /* intro blocks */
  .block-title { font-size: 23px; font-weight: 600; color: var(--navy); }
  .block-text { font-size: 14px; font-weight: 300; line-height: 20.6px; color: var(--body-grey); }
  .who-photo { left: 0; top: 781px; width: 607px; height: 510px; background: linear-gradient(180deg, var(--sky-a), var(--sky-b) 70%, var(--sky-a)); }
  .who { left: 733px; top: 928px; width: 256px; }
  .who .block-title { margin-bottom: 18px; }
  .want-photo { left: 610px; top: 1395px; width: 590px; height: 577px; background: linear-gradient(180deg, var(--haze-a), #9fb4c4 50%, var(--haze-b)); }
  .want { left: 226px; top: 1530px; width: 258px; text-align: right; }
  .want .block-title { margin-bottom: 18px; }

  /* overlay bands */
  .band-text { position: absolute; text-align: center; color: var(--white); }
  .band-text h2 { font-size: 23px; font-weight: 600; margin-bottom: 14px; }
  .band-text p { font-size: 14px; font-weight: 300; line-height: 20.6px; }
  .practice-photo { left: 0; top: 2078px; width: 1200px; height: 697px; background: linear-gradient(160deg, var(--dusk-a), #50608a 45%, var(--dusk-b)); }
  .practice { left: 250px; top: 2308px; width: 700px; }
  .practice p { width: 640px; margin: 0 auto; }

  /* goals */
  .goals-title { left: 0; top: 2856px; width: 1200px; text-align: center; font-size: 23px; font-weight: 600; }
  .goal { position: absolute; width: 300px; display: flex; flex-direction: column; align-items: center; text-align: center; }
  .goal-icon { width: 120px; height: 120px; margin-bottom: 46px; }
  .goal-label { font-size: 23px; font-weight: 400; line-height: 30px; color: var(--navy); }

  .achieved-photo { left: 0; top: 3825px; width: 1200px; height: 675px; background: linear-gradient(180deg, var(--sea-a), var(--sea-b)); }
  .achieved { left: 380px; top: 4084px; width: 440px; }

  /* footer */
  .site-footer { left: 0; top: 4500px; width: 1200px; height: 277px; background: var(--footer); }
  .site-footer .brand { left: 0; top: 52px; width: 1200px; flex-direction: column; gap: 10px; }
  .site-footer .nav { left: 0; top: 195px; width: 1200px; justify-content: center; font-size: 14px; }
  .copyright { position: absolute; left: 0; top: 240px; width: 1200px; text-align: center; font-size: 10px; color: var(--white); }
</style>
</head>
<body>

<header class="site-header">
  <div class="photo hero" role="img" aria-label="Sailor at the bow of a sailboat on a lake surrounded by mountains"></div>
  <div class="brand"><span class="brand-dot"></span><span class="brand-name">Verein Sail Brightly</span></div>
  <nav class="nav"><a class="current" href="#">Home</a><a href="#">About</a><a href="#">Sponsors</a><a href="#">Gallery</a></nav>
  <h1 class="abs hero-quote">Wir Können die Windrichtung nicht bestimmen, aber wir können die Segel richtig setzen!</h1>
  <p class="abs hero-author">Marcus Aurelian Vento</p>
</header>

<main>
  <div class="photo who-photo" role="img" aria-label="Three sailboats on blue water under a clear sky"></div>
  <section class="abs who">
    <h2 class="block-title">Wir sind...</h2>
    <p class="block-text">...trained social workers and experienced skippers who volunteer in the Sail Brightly association and organize a fleet for socially disadvantaged children and young people from central Upper Austria every year and set up the necessary financial resources.</p>
  </section>

  <section class="abs want">
    <h2 class="block-title">We want...</h2>
    <p class="block-text">..enabling children and young people who don't always have it easy in life to spend an unforgettable week in Croatia. It is precisely this shared experience that gives the children and young people a new zest for life and perspectives for their future. Through the reflection and also the care afterwards in the individual facilities, the children and young people can draw on this experience for a long time to come. This sustainability creates numerous pedagogical points of contact that represent a valuable basis for the achievement of goals.</p>
  </section>
  <div class="photo want-photo" role="img" aria-label="Sailboats gliding across hazy sunlit water"></div>

  <div class="photo practice-photo" role="img" aria-label="Sail and rigging of a boat at dusk over the sea"></div>
  <section class="band-text practice">
    <h2>Practical implementation of the pedagogical considerations</h2>
    <p>The participants are consciously involved in sailing activities. There are responsibilities for a wide variety of tasks in everyday life. A cooking and cleaning plan should help to take responsibility towards the group. The fact of steering a sailing ship alone fills many with great pride. Recurring activities on the ship require the involvement of every crew member. This gives everyone the feeling of being important to the community and everyone learns to take on this responsibility if they can. Sail Brightly offers an ideal training ground for social learning. The intensive confrontation with others and the group in a confined space offers a wide variety of opportunities to try out dealing with fellow human beings. All of these experiences can lead to self-esteem.</p>
  </section>

  <section class="project-goals">
    <h2 class="abs goals-title">project goals</h2>

    <div class="goal" style="left:63px;top:3093px;">
      <svg class="goal-icon" viewBox="0 0 120 120" aria-hidden="true">
        <circle cx="60" cy="60" r="56" fill="var(--icon-tint)"/>
        <path d="M60 86V36M40 56l20-20 20 20" fill="none" stroke="var(--icon-line)" stroke-width="6" stroke-linecap="round" stroke-linejoin="round"/>
      </svg>
      <p class="goal-label">Strengthening of self-esteem and social skills</p>
    </div>

    <div class="goal" style="left:447px;top:3093px;">
      <svg class="goal-icon" viewBox="0 0 120 120" aria-hidden="true">
        <circle cx="60" cy="60" r="56" fill="var(--icon-tint)"/>
        <path d="M37 61l15 15 31-32" fill="none" stroke="var(--icon-line)" stroke-width="7" stroke-linecap="round" stroke-linejoin="round"/>
      </svg>
      <p class="goal-label">Take responsibility for yourself and others</p>
    </div>

    <div class="goal" style="left:822px;top:3093px;">
      <svg class="goal-icon" viewBox="0 0 120 120" aria-hidden="true">
        <circle cx="60" cy="60" r="56" fill="var(--icon-tint)"/>
        <circle cx="48" cy="60" r="20" fill="none" stroke="var(--icon-line)" stroke-width="6"/>
        <circle cx="72" cy="60" r="20" fill="none" stroke="var(--icon-line)" stroke-width="6"/>
      </svg>
      <p class="goal-label">practicing tolerance</p>
    </div>

    <div class="goal" style="left:262px;top:3520px;">
      <svg class="goal-icon" viewBox="0 0 120 120" aria-hidden="true">
        <circle cx="60" cy="60" r="56" fill="var(--icon-tint)"/>
        <path d="M28 48h52M68 36l12 12-12 12M92 72H40M52 60L40 72l12 12" fill="none" stroke="var(--icon-line)" stroke-width="6" stroke-linecap="round" stroke-linejoin="round"/>
      </svg>
      <p class="goal-label">Development of non-violent conflict resolution strategies</p>
    </div>

    <div class="goal" style="left:661px;top:3520px;">
      <svg class="goal-icon" viewBox="0 0 120 120" aria-hidden="true">
        <circle cx="60" cy="60" r="56" fill="var(--icon-tint)"/>
        <path d="M60 30l8.8 18 19.7 2.9-14.3 13.9 3.4 19.6L60 75l-17.6 9.4 3.4-19.6-14.3-13.9L51.2 48z" fill="none" stroke="var(--icon-line)" stroke-width="5" stroke-linejoin="round"/>
      </svg>
      <p class="goal-label">Experiential Learning</p>
    </div>
  </section>

  <div class="photo achieved-photo" role="img" aria-label="Sailboat seen from behind on deep blue sea"></div>
  <section class="band-text achieved">
    <h2>Achieved goals</h2>
    <p>By experiencing a sailing week together, the "Sail Brightly fleet" creates ideal conditions under which the key objectives such as social integration and educational development of the children can be implemented in a concrete, efficient and professional manner and with a lasting effect.</p>
  </section>
</main>

<footer class="abs site-footer">
  <div class="brand"><span class="brand-dot"></span><span class="brand-name">Verein Sail Brightly</span></div>
  <nav class="nav"><a class="current" href="#">Home</a><a href="#">About</a><a href="#">Sponsors</a><a href="#">Gallery</a></nav>
  <p class="copyright">© Sailbrightly 2022</p>
</footer>

</body>
</html>
```